We operate a niche online Job Board in Australia. The website is called 'Harbourline Careers Australia' and is used by Christian Employers to advertise their job vacancies.
I would like a business card that identifies with our website (www.harbourlinecareers.com.au). We would like the same colors and fonts used on our business card from our website. When people look at our business card we want them to be able to recognise it from the website.
We want the web address to be dominant.
Updates
We are liking those that use white space as well as the blue and orange and those that highlight the url.
We now have 60 designs and therefore will not wait for the Sunday deadline to make a decision. We have a few we like.
The ones we like are:
- bold
- creative
- colorful (blue orange and white)
- some white space
- no boxes or borders
- font the same as our website
- reflects the look of our website
We will make a final decision in the next 6 hours so please if you think you have something to offer then get it in within the next 6 hours. If you think you will leave it till later you will miss out. Thanks to all those who have responded with some great designs, sorry we can't reward all of you!
Industry/Entity Type
Business
Contact Information for Business Card
Harbourline Careers Australia
www.harbourlinecareers.com.au
Gregory Palliser
CEO
Phone: 1300 574 816
Mobile: 0412 937215
Fax: (03) 9172 4463
email: gregory@harbourlinecareers.com.au
Requirements
Should not have
- We do not want a cross or any cliche christian images.

```html
<!DOCTYPE html>
<html lang="en">
<head>
<meta charset="utf-8">
<title>Harbourline Careers Australia – Business Card</title>
<link rel="stylesheet" href="https://fonts.googleapis.com/css2?family=Tinos:wght@400;700&family=Open+Sans:wght@400&display=swap">
<style>
  :root {
    --stage: #b0aeaf;
    --card-white: #ffffff;
    --navy: #2e2a6f;
    --orange: #f58220;
    --text-light: #ffffff;
  }
  html, body {
    margin: 0;
    padding: 0;
    width: 1200px;
    height: 900px;
    overflow: hidden;
    background: var(--stage);
  }
  .canvas {
    position: relative;
    width: 1200px;
    height: 900px;
  }
  .business-card {
    position: absolute;
    left: 120px;
    top: 162px;
    width: 960px;
    height: 576px;
    border-radius: 30px;
    overflow: hidden;
    background: var(--card-white);
    box-shadow: 0 12px 30px rgba(0, 0, 0, 0.25);
  }
  .identity {
    position: absolute;
    right: 56px;
    top: 44px;
    text-align: right;
  }
  .person-name {
    margin: 0;
    font-family: "Tinos", serif;
    font-weight: 700;
    font-size: 31px;
    color: var(--navy);
  }
  .person-role {
    margin: 10px 0 0;
    font-family: "Tinos", serif;
    font-weight: 700;
    font-size: 20px;
    color: var(--orange);
  }
  .brand-name {
    position: absolute;
    left: 150px;
    top: 140px;
    margin: 0;
    font-family: "Tinos", serif;
    font-weight: 400;
    font-size: 50px;
    letter-spacing: 0.2px;
    color: var(--navy);
    white-space: nowrap;
  }
  .web-address {
    position: absolute;
    left: 150px;
    top: 204px;
    margin: 0;
    font-family: "Open Sans", sans-serif;
    font-weight: 400;
    font-size: 41px;
    color: var(--orange);
    white-space: nowrap;
  }
  .accent-band {
    position: absolute;
    left: 0;
    top: 270px;
    width: 100%;
    height: 22px;
    background: var(--orange);
  }
  .contact-panel {
    position: absolute;
    left: 0;
    top: 292px;
    width: 100%;
    height: 284px;
    background: var(--navy);
  }
  .contact-list {
    position: absolute;
    left: 64px;
    top: 70px;
    margin: 0;
    padding: 0;
    list-style: none;
  }
  .contact-item {
    display: flex;
    align-items: center;
    height: 44px;
    font-family: "Tinos", serif;
    font-size: 31px;
    color: var(--text-light);
  }
  .contact-icon {
    width: 34px;
    height: 30px;
    margin-right: 8px;
    flex: none;
  }
</style>
</head>
<body>
<div class="canvas">
  <section class="business-card" aria-label="Business card for Harbourline Careers Australia">
    <div class="identity">
      <p class="person-name">Gregory Palliser</p>
      <p class="person-role">CEO</p>
    </div>

    <p class="brand-name">Harbourline Careers Australia</p>
    <p class="web-address">www.harbourlinecareers.com.au</p>

    <div class="accent-band"></div>

    <div class="contact-panel">
      <ul class="contact-list">
        <li class="contact-item">
          <svg class="contact-icon" viewBox="0 0 34 30" aria-hidden="true">
            <path d="M4 9 Q17 1 30 9 L28 13 L23 12 L22 9 Q17 7 12 9 L11 12 L6 13 Z" fill="var(--orange)"/>
            <path d="M9 14 L25 14 L29 27 L5 27 Z" fill="var(--orange)"/>
            <circle cx="17" cy="20" r="3.5" fill="var(--navy)"/>
          </svg>
          <span>1300 574 816</span>
        </li>
        <li class="contact-item">
          <svg class="contact-icon" viewBox="0 0 34 30" aria-hidden="true">
            <path d="M8 4 L13 4 L15 10 L12 12 Q14 18 20 21 L22 18 L28 20 L28 25 Q26 28 22 27 Q10 23 6 10 Q5 6 8 4 Z" fill="var(--orange)"/>
          </svg>
          <span>0412 937 215</span>
        </li>
        <li class="contact-item">
          <svg class="contact-icon" viewBox="0 0 34 30" aria-hidden="true">
            <rect x="3" y="7" width="28" height="18" fill="none" stroke="var(--orange)" stroke-width="2"/>
            <path d="M3 7 L17 18 L31 7" fill="none" stroke="var(--orange)" stroke-width="2"/>
          </svg>
          <span>gregory@harbourlinecareers.com.au</span>
        </li>
      </ul>
    </div>
  </section>
</div>
</body>
</html>
```